4 Page 8.5x11 Price List & Flyer

Our main product price list that goes out to all of our dealers and distributors both in print and PDF. Should be clean and bright, easy to read and attract attention.
Updates

Target Market(s)

Dealers and distributors of sports card holders, photo holders, sports memorabilia display cases, etc.

Industry/Entity Type

Product

Requirements
Must have
• Paperleaf Crown logo, photos

```html
<!DOCTYPE html>
<html lang="en">
<head>
<meta charset="utf-8">
<title>Top Load Cases – Paperleaf Crown Price List</title>
<link rel="stylesheet" href="https://fonts.googleapis.com/css2?family=Great+Vibes&family=Arimo:wght@400;700&display=swap">
<style>
  :root {
    --sky-top: #7fb2c2;
    --sky-deep: #3f7486;
    --floor: #a3a6a8;
    --floor-light: #c4c7c8;
    --frame-black: #0d0d0d;
    --frame-gold: #d9a93a;
    --gold-light: #f3d27a;
    --paper: #ffffff;
    --ink: #111111;
    --rule: #222222;
    --pack-dark: #1a1a1a;
    --pack-mid: #3a3a3a;
  }
  * { box-sizing: border-box; margin: 0; padding: 0; }
  html, body { width: 1200px; height: 1200px; overflow: hidden; }
  body {
    position: relative;
    font-family: "Arimo", Arial, sans-serif;
    color: var(--ink);
    background:
      linear-gradient(180deg, var(--sky-top) 0%, var(--sky-deep) 62%, var(--floor) 65%, var(--floor-light) 100%);
  }
  .frame { position: absolute; inset: 0; }
  .sheet-title {
    position: absolute;
    top: 118px; left: 0; width: 1200px;
    text-align: center;
    font-family: "Great Vibes", cursive;
    font-size: 78px;
    line-height: 1;
    color: var(--ink);
  }
  .product-photo {
    position: absolute;
    top: 86px;
    width: 84px; height: 134px;
    border-radius: 3px;
    background: linear-gradient(180deg, var(--pack-mid) 0%, var(--pack-dark) 55%, #000 100%);
  }
  .product-photo.left { left: 190px; }
  .product-photo.right { left: 898px; }
  table { position: absolute; border-collapse: collapse; table-layout: fixed; }
  td, th { border: 1.5px solid var(--rule); white-space: nowrap; overflow: hidden; }
  .price-main { top: 284px; left: 165px; width: 868px; }
  .price-main th { height: 30px; font-size: 21px; font-weight: 400; text-align: center; }
  .price-main td { height: 26.5px; font-size: 17px; padding: 0 4px; line-height: 1; }
  .price-extra { top: 886px; left: 167px; width: 862px; }
  .price-extra th { height: 24px; font-size: 17px; font-weight: 400; text-align: center; }
  .price-extra td { height: 22.4px; font-size: 14px; padding: 0 4px; line-height: 1; }
  .c { text-align: center; }
  .r { text-align: right; }
</style>
</head>
<body>
  <svg class="frame" width="1200" height="1200" viewBox="0 0 1200 1200" aria-hidden="true">
    <polygon fill="var(--frame-black)" points="55,43 1145,43 1145,545 1180,588 1145,631 1145,1157 55,1157 55,631 20,588 55,545"/>
    <polygon fill="none" stroke="var(--frame-gold)" stroke-width="5" points="67,55 1133,55 1133,549 1163,588 1133,627 1133,1145 67,1145 67,627 37,588 67,549"/>
    <polygon fill="none" stroke="var(--gold-light)" stroke-width="1.5" points="72,60 1128,60 1128,552 1156,588 1128,624 1128,1140 72,1140 72,624 44,588 72,552"/>
    <polygon fill="var(--paper)" points="80,68 1120,68 1120,556 1146,588 1120,620 1120,1132 80,1132 80,620 54,588 80,556"/>
  </svg>

  <div class="product-photo left" role="img" aria-label="Product photo: black retail pack of card team bags"></div>
  <div class="product-photo right" role="img" aria-label="Product photo: black retail pack of card team bags"></div>

  <h1 class="sheet-title">Top Load Cases</h1>

  <table class="price-main">
    <colgroup><col style="width:80px"><col style="width:225px"><col style="width:255px"><col style="width:157px"><col style="width:151px"></colgroup>
    <thead><tr><th>Size</th><th>Description</th><th>Pack/Case/Weight</th><th>$250 Min</th><th>$1,500 Min</th></tr></thead>
    <tbody>
      <tr><td>3x4</td><td>Clear</td><td class="c">25/1000/18 lbs</td><td class="c">$28/case</td><td class="c">$25/case</td></tr>
      <tr><td>3x4</td><td>“Rookie” Gold</td><td class="c">25/1000/18 lbs</td><td class="c">$37/case</td><td class="c">$33/case</td></tr>
      <tr><td>3x4</td><td>Color Border</td><td class="c">25/1000/18 lbs</td><td class="c">$37/case</td><td class="c">$33/case</td></tr>
      <tr><td>3x4</td><td>1.5mm – 60 Pt.</td><td class="c">25/1000/23 lbs</td><td class="c">$55/case</td><td class="c">$49/case</td></tr>
      <tr><td>3x4</td><td>2.5mm – 100 Pt.</td><td class="c">25/500/12 lbs</td><td class="c">$39/case</td><td class="c">$34/case</td></tr>
      <tr><td>3x4</td><td>3.5mm – 140 Pt.</td><td class="c">10/500/14 lbs</td><td class="c">$60/case</td><td class="c">$55/case</td></tr>
      <tr><td>3x4</td><td>5mm – 190 Pt.</td><td class="c">5/250/8 lbs</td><td class="c">$35/case</td><td class="c">$30/case</td></tr>
      <tr><td>3x4</td><td>7mm – 240 Pt.</td><td class="c">5/250/10 lbs</td><td class="c">$41.50/case</td><td class="c">$37.50/case</td></tr>
      <tr><td>4x6</td><td>Photo</td><td class="c">25/500/25 lbs</td><td class="c">$55/case</td><td class="c">$47.50/case</td></tr>
      <tr><td>6x4</td><td>Side Load Photo</td><td class="c">25/500/25 lbs</td><td class="c">$55/case</td><td class="c">$47.50/case</td></tr>
      <tr><td>5x7</td><td>Photo</td><td class="c">25/500/33 lbs</td><td class="c">$69/case</td><td class="c">$59/case</td></tr>
      <tr><td>6x9</td><td>Photo</td><td class="c">25/250/19 lbs</td><td class="c">$55/case</td><td class="c">$49/case</td></tr>
      <tr><td>8x10</td><td>Photo</td><td class="c">25/250/34 lbs</td><td class="c">$80/case</td><td class="c">$75/case</td></tr>
      <tr><td>8.5x11</td><td>Photo</td><td class="c">25/250/39 lbs</td><td class="c">$97.50/case</td><td class="c">$92.50/case</td></tr>
      <tr><td>11x14</td><td>Photo</td><td class="c">25/100/34 lbs</td><td class="c">$65/case</td><td class="c">$59/case</td></tr>
      <tr><td>11x17</td><td>Photo</td><td class="c">25/100/42 lbs</td><td class="c">$79/case</td><td class="c">$75/case</td></tr>
      <tr><td>16x20</td><td>Photo</td><td class="c">10/50/32 lbs</td><td class="c">$62.50/case</td><td class="c">$55/case</td></tr>
      <tr><td>24x36</td><td>Poster</td><td class="c">1/10/19 lbs</td><td class="c">$34/case</td><td class="c">$30/case</td></tr>
      <tr><td>29x43</td><td>Poster/Sheet</td><td class="c">1/10/28 lbs</td><td class="c">$49/case</td><td class="c">$45/case</td></tr>
    </tbody>
  </table>

  <table class="price-extra">
    <colgroup><col style="width:226px"><col style="width:172px"><col style="width:198px"><col style="width:129px"><col style="width:137px"></colgroup>
    <thead><tr><th>Size</th><th>Description</th><th>Pack/Case/Weight</th><th>$250 Min</th><th>$1,500 Min</th></tr></thead>
    <tbody>
      <tr><td>Pennant</td><td></td><td class="r">10/50/19 lbs</td><td class="c">$75.00/case</td><td class="c">$65/case</td></tr>
      <tr><td>Thick Magazine 7mm</td><td></td><td class="r">10/50/12 lbs.</td><td class="c">$41/case</td><td class="c">$35/case</td></tr>
      <tr><td>Super Thick Mag 10mm</td><td></td><td class="r">5/50/15 lbs</td><td class="c">$47.50/case</td><td class="c">$42/case</td></tr>
      <tr><td>Ticket (3 3/8”x 7 ¼”)</td><td>Photo</td><td class="r">25/500/28 lbs</td><td class="c">$65/case</td><td class="c">$55/case</td></tr>
      <tr><td>Reg.</td><td>Currency</td><td class="r">25/500/21 lbs</td><td class="c">$55/case</td><td class="c">$49/case</td></tr>
      <tr><td>Large</td><td>Currency</td><td class="r">25/250/14 lbs</td><td class="c">$32.50/case</td><td class="c">$28.75/case</td></tr>
    </tbody>
  </table>
</body>
</html>
```